Modern business card design for professional copywriter

I'd like a business card design that I can use to have my cards printed out by tavrel.com as a squared corners business card (see artwork and design guidelines here: https://help.tavrel.com/hc/en-gb/sections/300481762-TAVREL-Product-Templates)

The design should be clean and modern and reflect the colours, tone and branding on my website: https://gretafolvane.com.au

Target Market(s)

Professionals, B2B small business owners

Industry/Entity Type

Business

Contact Information for Business Card

Greta Folvane
m: 0427 954 368
e: greta@gretafolvane.com.au
w: gretafolvane.com.au

Font styles to use
Sans Serif

Requirements
Must have
• Tagline: "Clear copy for bright small business owners"
• Brand colours: fd8000, 009984, 666666 and black
Nice to have

```html
<!DOCTYPE html>
<html lang="en">
<head>
<meta charset="utf-8">
<title>Greta Folvane – Business Card</title>
<link href="https://fonts.googleapis.com/css2?family=Open+Sans:wght@400;600;700&display=swap" rel="stylesheet">
<style>
  :root {
    --teal: #169a84;
    --orange: #f58220;
    --white: #ffffff;
    --bg-top: #383838;
    --bg-bottom: #4f4f4f;
  }
  * { margin: 0; padding: 0; box-sizing: border-box; }
  html, body { width: 1200px; height: 900px; overflow: hidden; }
  body {
    background: linear-gradient(180deg, var(--bg-top), var(--bg-bottom));
    font-family: "Open Sans", sans-serif;
    position: relative;
  }
  .card {
    position: absolute;
    top: 306px;
    width: 440px;
    height: 271px;
    overflow: hidden;
  }
  .card-front { left: 149px; background: var(--white); }
  .card-back { left: 608px; background: var(--teal); }

  .front-wave { position: absolute; inset: 0; width: 100%; height: 100%; }

  .brand {
    position: absolute;
    display: flex;
    align-items: center;
    gap: 8px;
    font-weight: 600;
    white-space: nowrap;
    letter-spacing: -0.5px;
  }
  .brand-mark { width: 14px; height: 14px; flex: none; }
  .card-front .brand { right: 22px; top: 52px; font-size: 32px; color: var(--teal); }
  .card-front .brand-mark { background: var(--orange); }
  .card-back .brand { left: 0; right: 0; justify-content: center; top: 116px; font-size: 36px; color: var(--white); }
  .card-back .brand-mark { background: var(--white); border-radius: 50%; }

  .holder-name {
    position: absolute;
    left: 24px; top: 171px;
    color: var(--white);
    font-size: 17px;
    font-weight: 400;
    letter-spacing: 0.3px;
  }
  .contact-list {
    position: absolute;
    left: 25px; top: 203px;
    list-style: none;
    color: var(--white);
    font-size: 12px;
    line-height: 16px;
  }
  .contact-list li { display: flex; align-items: center; gap: 7px; }
  .contact-list svg { width: 9px; height: 9px; fill: var(--white); flex: none; }

  .tagline-band {
    position: absolute;
    left: 0; right: 0; top: 208px;
    height: 41px;
    background: var(--orange);
    color: var(--white);
    font-weight: 700;
    font-size: 13px;
    text-transform: uppercase;
    display: flex; align-items: center; justify-content: center;
  }
</style>
</head>
<body>
  <section class="card card-front" aria-label="Business card front">
    <svg class="front-wave" viewBox="0 0 440 271" preserveAspectRatio="none" aria-hidden="true">
      <path d="M0 146 C150 138 300 170 440 212 L440 271 L0 271 Z" fill="var(--teal)"/>
      <path d="M138 148 C250 146 360 158 440 168 L440 196 C370 184 290 166 138 148 Z" fill="var(--orange)" stroke="var(--white)" stroke-width="4"/>
    </svg>
    <div class="brand"><span class="brand-mark"></span>Greta Folvane</div>
    <h1 class="holder-name">GRETA FOLVANE</h1>
    <ul class="contact-list">
      <li><svg viewBox="0 0 10 10"><path d="M2.5 0h5a1 1 0 0 1 1 1v8a1 1 0 0 1-1 1h-5a1 1 0 0 1-1-1V1a1 1 0 0 1 1-1zm.5 1.3v6h4v-6z"/></svg>0427 954 368</li>
      <li><svg viewBox="0 0 10 10"><path d="M0 2h10v6H0z M0.6 2.4 5 5.6 9.4 2.4" stroke="#169a84" stroke-width="0.8"/></svg>greta@gretafolvane.com.au</li>
      <li><svg viewBox="0 0 10 10"><circle cx="5" cy="5" r="4.6"/></svg>gretafolvane.com.au</li>
    </ul>
  </section>

  <section class="card card-back" aria-label="Business card back">
    <div class="brand"><span class="brand-mark"></span>Greta Folvane</div>
    <p class="tagline-band">Clear copy for bright small business owners</p>
  </section>
</body>
</html>
```